Tor Ridge Wine Club-The Onyx Roll

We are a new aspirational brand of fine Tasmania Wine. We need a commitment club poster which appeals to the ego.We have one opportunity to get customers to sign up and that is when they visit at the cellar door. This club is the core of our business.

The brand is a clean, pure , simple brand, black and white very sophiscated.
This is a top end product.

Our Commitment Club is named The Onyx Roll which is a play on words. Tradionally The Onyx Roll is a list of people that you dont want to do business with. So we are turning this on its had.

You need to make this poster sharp, desirable, possibly sexy but masculine. Im thinking Felix Crane . It doesnt matter the client will be 40 up fashion consious looking for something new , exclusive , something there peers don't have.

I dont like busy! make it clean clear and basically undeniable. The client must not be able to resist the offer.

www.torridgevines.com.au

Reason: Internet problems so cant get to respond and offer comment in a timely manner

Appreciator 40-60 male wants to be recognised fashion consious sophiscated has money and wants to part of something exclusive.

A feeling that you are part of something that only a few are. Exclusive

Maybe an imagine of beautiful people 30/40ish I want to be drinking Tor Wine / in The Onyx Roll

Fashion

Must have
• Tor Ridge Logo
TOR Bottles images

We produce only 1600 cases of wine each vintage. Therefore we have limited membership 001-999 for our club.
Award Winning Wines available exclusively from us.

Gold Member
We will reserve 2 cases of our limited vintage, to be delivered to you in May and Oct.
Single varietal or mixed cases. You receive a 15% discount.

Silver Member
We will reserve 1 case of our limited vintage to be delivered to you 6 bottles in May and 6 in Oct.
Single varietal or mixed cases. You receive a 10% discount.

To you exclusively from us not, available from any other retailers.

You will be invited to Onyx Roll Only Events and Tastings.
You will get preferential access to new and limited releases.
Members will be entered in a bi annual draw to win a 2 night stay here at the Tor Weavers Cottage on the Freycinet Coast Tasmania.

• VIP stamps,gimacs, anything that cheapens our brand.

We do not like busy posters please have white space

```html
<!DOCTYPE html>
<html lang="en">
<head>
<meta charset="utf-8">
<title>The Onyx Roll — Tor Ridge Wine Club</title>
<link rel="stylesheet" href="https://fonts.googleapis.com/css2?family=Antonio:wght@100;300;700&family=Arimo:wght@400;700&display=swap">
<style>
  :root {
    --ink: #000000;
    --paper: #ffffff;
    --gold: #b3985d;
    --gold-light: #c9b07a;
    --rule: #ffffff;
  }
  html, body { margin: 0; padding: 0; overflow: hidden; background: var(--paper); }
  .canvas { width: 848px; height: 1200px; overflow: hidden; position: relative; background: var(--paper); }
  .poster { width: 800px; height: 1132px; position: absolute; left: 0; top: 0; transform: scale(1.06); transform-origin: 0 0; font-family: "Arimo", Arial, sans-serif; }
  .banner-shape { position: absolute; left: 0; top: 0; width: 800px; height: 760px; }
  .abs { position: absolute; }
  .tag { left: 272px; top: 50px; width: 256px; height: 26px; background: var(--gold); color: var(--ink);
    font-family: "Antonio", sans-serif; font-weight: 300; font-size: 17px; letter-spacing: 11px; text-align: center; line-height: 26px; text-indent: 11px; }
  .tag-rule { left: 272px; top: 82px; width: 256px; height: 1px; background: var(--rule); }
  .title { left: 0; top: 90px; width: 800px; height: 150px; margin: 0; }
  .title svg { display: block; width: 800px; height: 150px; }
  .title text { fill: var(--paper); font-family: "Antonio", sans-serif; font-size: 122px; }
  .title .thin { font-weight: 100; }
  .title .bold { font-weight: 700; }
  .dots { left: 122px; top: 265px; width: 556px; border-top: 3px dotted var(--paper); }
  .place { top: 318px; color: var(--paper); font-family: "Antonio", sans-serif; font-weight: 100; font-size: 27px; letter-spacing: 5px; }
  .place.left { left: 120px; }
  .place.right { left: 568px; }
  .glass { top: 290px; width: 32px; height: 82px; }
  .glass.left { left: 268px; }
  .glass.right { left: 503px; }
  .brand-mark { left: 320px; top: 310px; width: 160px; text-align: center; color: var(--paper);
    font-family: "Antonio", sans-serif; font-weight: 300; font-size: 40px; letter-spacing: 1px; }
  .club-line { left: 0; top: 412px; width: 800px; text-align: center; color: var(--gold-light);
    font-weight: 700; font-size: 13.5px; letter-spacing: .2px; }
  .hr { left: 110px; width: 570px; height: 1px; background: var(--rule); }
  .tier-name { left: 112px; color: var(--paper); font-family: "Antonio", sans-serif; font-weight: 300; font-size: 21px; letter-spacing: .5px; }
  .tier-list { left: 300px; color: var(--paper); font-size: 12px; line-height: 15px; margin: 0; padding: 0; list-style: none; }
  .tier-list li::before { content: "• "; }
  .perks { left: 110px; top: 548px; width: 580px; text-align: center; color: var(--paper); font-size: 12px; line-height: 18px; margin: 0; }
  .perks strong { font-weight: 700; }
  .url { left: 0; top: 624px; width: 800px; text-align: center; color: var(--paper); font-size: 11px; letter-spacing: 9.5px; text-indent: 9px; }
  .bottle { top: 742px; width: 92px; height: 390px; border-radius: 20px 20px 0 0; }
  .bottle.sauvignon { left: 192px; background: linear-gradient(90deg, #c7c43a, #e7e46a 40%, #a9a62a); }
  .bottle.pinot-noir { left: 300px; background: linear-gradient(90deg, #3a0710, #7a1524 40%, #2a040a); }
  .bottle.pinot-gris { left: 408px; background: linear-gradient(90deg, #b9ba2c, #dedd5e 40%, #9d9b22); }
  .bottle.rose { left: 516px; background: linear-gradient(90deg, #e06a55, #f6a58e 40%, #d25a48); }
  .tagline { left: 48px; top: 814px; color: var(--ink); font-family: "Antonio", sans-serif; font-weight: 100; font-size: 27px; line-height: 28px; letter-spacing: 1px; }
  .footer-mark { left: 636px; top: 812px; width: 130px; text-align: center; color: var(--ink);
    font-family: "Antonio", sans-serif; font-weight: 300; font-size: 38px; }
</style>
</head>
<body>
<div class="canvas">
  <div class="poster">
    <svg class="banner-shape" viewBox="0 0 800 760" aria-hidden="true">
      <polygon points="62,596 738,596 738,606 400,752 62,606" fill="#b3985d"/>
      <polygon points="48,0 752,0 752,590 400,738 48,590" fill="#000"/>
    </svg>

    <div class="abs tag">INTRODUCING</div>
    <div class="abs tag-rule"></div>

    <h1 class="abs title" aria-label="The Onyx Roll">
      <svg viewBox="0 0 800 150" aria-hidden="true">
        <text class="thin" x="120" y="135" textLength="120" lengthAdjust="spacingAndGlyphs">THE</text>
        <text class="bold" x="268" y="135" textLength="252" lengthAdjust="spacingAndGlyphs">ONYX</text>
        <text class="thin" x="548" y="135" textLength="132" lengthAdjust="spacingAndGlyphs">ROLL</text>
      </svg>
    </h1>
    <div class="abs dots"></div>

    <div class="abs place left">CRANBROOK</div>
    <svg class="abs glass left" viewBox="0 0 32 82" aria-hidden="true">
      <path d="M4 2 Q2 28 16 36 Q30 28 28 2 Z" fill="none" stroke="#fff" stroke-width="2"/>
      <path d="M4 16 Q5 30 16 34 Q27 30 28 16 Z" fill="#fff"/>
      <line x1="16" y1="36" x2="16" y2="72" stroke="#fff" stroke-width="2"/>
      <path d="M6 78 Q16 70 26 78" fill="#fff" stroke="#fff" stroke-width="2"/>
    </svg>
    <div class="abs brand-mark">Tor Ridge</div>
    <svg class="abs glass right" viewBox="0 0 32 82" aria-hidden="true">
      <path d="M4 2 Q2 28 16 36 Q30 28 28 2 Z" fill="none" stroke="#fff" stroke-width="2"/>
      <path d="M4 16 Q5 30 16 34 Q27 30 28 16 Z" fill="#fff"/>
      <line x1="16" y1="36" x2="16" y2="72" stroke="#fff" stroke-width="2"/>
      <path d="M6 78 Q16 70 26 78" fill="#fff" stroke="#fff" stroke-width="2"/>
    </svg>
    <div class="abs place right">TASMANIA</div>

    <div class="abs club-line">EXCLUSIVE WINE CLUB MEMBERSHIP FROM THE AWARD-WINNING TOR RIDGE</div>

    <div class="abs hr" style="top:443px"></div>
    <div class="abs tier-name" style="top:450px">GOLD MEMBERSHIP:</div>
    <ul class="abs tier-list" style="top:451px">
      <li>1 case of Tor Ridge’s limited vintage (delivered May and October)</li>
      <li>receive a 15% discount</li>
    </ul>
    <div class="abs hr" style="top:489px"></div>
    <div class="abs tier-name" style="top:496px">SILVER MEMBERSHIP:</div>
    <ul class="abs tier-list" style="top:497px">
      <li>1 case of Tor Ridge’s limited vintage (delivered May and October)</li>
      <li>receive a 10% discount</li>
    </ul>
    <div class="abs hr" style="top:535px"></div>

    <p class="abs perks">Membership also includes exclusive access to pre-release offers &nbsp;•&nbsp; invitations to member-only tasting and events &nbsp;•&nbsp; entry into the bi-annual draw to win a 2 night stay at the Tor Weavers Cottage on the Freycinet Coast Tasmania. <strong>VISIT OUR WEBSITE FOR FULL DETAILS.</strong></p>

    <div class="abs url">WWW.TORRIDGEVINES.COM.AU</div>

    <div class="abs bottle sauvignon" role="img" aria-label="Photograph of a Tor Ridge 2011 Sauvignon Blanc bottle"></div>
    <div class="abs bottle pinot-noir" role="img" aria-label="Photograph of a Tor Ridge 2011 Pinot Noir bottle"></div>
    <div class="abs bottle pinot-gris" role="img" aria-label="Photograph of a Tor Ridge 2011 Pinot Gris bottle"></div>
    <div class="abs bottle rose" role="img" aria-label="Photograph of a Tor Ridge 2011 Rosé bottle"></div>

    <div class="abs tagline">EXPERIENCE<br>TASMANIA...</div>
    <div class="abs footer-mark">Tor Ridge</div>
  </div>
</div>
</body>
</html>
```